Dorsey and Partners Outpatient Imaging

1. flyer/rack card size, front and back for imaging services advertisement. Color design. Text file and one chest xray and one hand radiograph hopefully. Clean and easy to read. 2. clear to read title about "Outpatient imaging services" 3. Only using images and text provided. This is a radiology group offering web based image interpretation to physicians in the community.

Target Market(s)

Referring outpatient physicians

Industry/Entity Type

Medical Imaging

Font styles to use
Serif

Requirements
Must have
• preferably one picture, easy to read design
Nice to have
• both a hand and chest xray would be nice.

```html
<!DOCTYPE html>
<html lang="en">
<head>
<meta charset="utf-8">
<title>Dorsey and Partners Outpatient Imaging – Flyer</title>
<link href="https://fonts.googleapis.com/css2?family=Raleway:wght@400;500;600;700&display=swap" rel="stylesheet">
<style>
  :root {
    --brand-red: #a10e12;
    --tab-dark: #3d3d3f;
    --band-gray: #d3d3d5;
    --text: #4a4a4a;
    --stage: #4b4b4d;
    --white: #ffffff;
  }
  * { box-sizing: border-box; margin: 0; padding: 0; }
  html, body { width: 1200px; height: 1200px; overflow: hidden; background: var(--stage); font-family: "Raleway", sans-serif; }
  .canvas { position: relative; width: 1200px; height: 1200px; }

  .page { position: absolute; top: 250px; width: 541px; height: 701px; background: var(--white); overflow: hidden; color: var(--text); }
  .page--front { left: 54px; }
  .page--back { left: 606px; }

  .abs { position: absolute; }

  .brand { left: 40px; top: 68px; color: var(--brand-red); font-family: "Raleway", sans-serif; font-weight: 500; font-size: 22px; line-height: 25px; letter-spacing: 0.5px; text-transform: uppercase; }

  .photo { position: absolute; }
  .photo--reading-room { left: 0; top: 117px; width: 332px; height: 188px; background: linear-gradient(135deg, #6f6a66 0%, #b9b2ab 45%, #3e3f45 100%); }
  .photo--mammography { left: 332px; top: 117px; width: 209px; height: 188px; background: linear-gradient(160deg, #e7e4df 0%, #c9c6c1 55%, #a8a39c 100%); }
  .photo--physician { left: 374px; top: 421px; width: 167px; height: 280px; background: linear-gradient(180deg, #f3f3f3 0%, #e4e6ea 60%, #c9ced6 100%); }
  .photo--family { left: 0; top: 248px; width: 324px; height: 170px; background: linear-gradient(120deg, #e9d7bf 0%, #f2e6d5 40%, #c9a98a 100%); }

  .services-band { left: 0; top: 305px; width: 541px; height: 128px; background: var(--band-gray); }
  .services-title { left: 114px; top: 305px; width: 312px; height: 21px; }
  .services-title span { position: absolute; inset: 0; display: flex; align-items: center; justify-content: center; color: var(--white); font-weight: 600; font-size: 10.5px; letter-spacing: 0.2px; }
  .services-col { top: 337px; width: 150px; list-style: none; }
  .services-col li { position: relative; padding-left: 12px; margin-bottom: 5px; font-size: 8.3px; line-height: 10.5px; font-weight: 600; color: #3a3a3a; text-transform: uppercase; }
  .services-col li::before { content: ""; position: absolute; left: 0; top: 1px; width: 8px; height: 8px; border: 1.2px solid var(--brand-red); border-radius: 50%; }
  .services-col li::after { content: ""; position: absolute; left: 3px; top: 2px; width: 2.5px; height: 4.5px; border-right: 1.4px solid var(--brand-red); border-bottom: 1.4px solid var(--brand-red); transform: rotate(40deg); }
  .col-1 { left: 32px; } .col-2 { left: 200px; } .col-3 { left: 368px; }
  .col-divider { top: 340px; width: 2px; height: 85px; background: #bdbdc0; }

  .section-tab { height: 34px; }
  .section-tab span { position: absolute; left: 32px; top: 0; height: 100%; display: flex; align-items: center; color: var(--white); font-weight: 600; font-size: 13px; letter-spacing: 0.2px; text-transform: uppercase; }

  .body-copy { font-size: 10.4px; line-height: 15.2px; color: var(--text); }
  .body-copy--small { font-size: 9.4px; line-height: 14.2px; }

  .footer-wave { left: 0; bottom: 0; width: 541px; height: 120px; }
  .contact { color: var(--white); }
  .contact p { font-size: 11px; line-height: 13px; }
  .contact .contact-line { margin-top: 3px; font-weight: 700; font-size: 16px; line-height: 20px; display: flex; align-items: center; gap: 5px; }
  .contact--right { text-align: right; }
  .contact--right .contact-line { justify-content: flex-end; }
  .icon { width: 14px; height: 14px; flex: none; }

  .headline { left: 341px; top: 278px; width: 170px; font-size: 18.5px; line-height: 20.5px; font-weight: 500; color: #565658; text-transform: uppercase; }
  .headline-box { left: 324px; top: 248px; width: 217px; height: 170px; background: var(--band-gray); }
</style>
</head>
<body>
<main class="canvas">

  <!-- FRONT -->
  <section class="page page--front">
    <div class="abs brand">Dorsey and<br>Partners, P.C.</div>

    <div class="photo photo--reading-room" role="img" aria-label="Smiling radiologist at a reading station with MRI scans on monitors"></div>
    <div class="photo photo--mammography" role="img" aria-label="Technologist standing beside a mammography unit"></div>

    <div class="abs services-band"></div>
    <svg class="abs services-title" viewBox="0 0 312 21" preserveAspectRatio="none" aria-hidden="true"><polygon points="0,0 312,0 296,21 16,21" fill="var(--brand-red)"/></svg>
    <div class="abs services-title"><span>COMPREHENSIVE RADIOLOGICAL SERVICES:</span></div>

    <ul class="abs services-col col-1">
      <li>Mammography and<br>women's imaging</li>
      <li>Image guided breast and<br>thyroid biopsies</li>
      <li>Oncology imaging</li>
      <li>Advanced breast MRI</li>
      <li>Ultrasound</li>
    </ul>
    <div class="abs col-divider" style="left:180px"></div>
    <ul class="abs services-col col-2">
      <li>Orthopedic and sports<br>imaging</li>
      <li>Brain and spine imaging</li>
      <li>CT scanning</li>
      <li>Balloon kyphoplasty</li>
      <li>Peripheral joint<br>injections</li>
    </ul>
    <div class="abs col-divider" style="left:350px"></div>
    <ul class="abs services-col col-3">
      <li>Advanced MRI / MRA</li>
      <li>Teleradiology</li>
      <li>Interventional oncology<br>therapy</li>
      <li>Complete vascular<br>interventional services</li>
    </ul>

    <svg class="abs footer-wave" viewBox="0 0 541 120" preserveAspectRatio="none" aria-hidden="true"><path d="M0,22 C120,-2 240,0 541,68 L541,120 L0,120 Z" fill="var(--brand-red)"/></svg>
    <div class="photo photo--physician" role="img" aria-label="Young physician in a white coat with a stethoscope, arms crossed"></div>

    <svg class="abs section-tab" style="left:0;top:433px;width:282px" viewBox="0 0 282 34" preserveAspectRatio="none" aria-hidden="true"><polygon points="0,4 282,4 262,30 0,30" fill="var(--tab-dark)"/></svg>
    <div class="abs section-tab" style="left:0;top:433px;width:282px"><span>Why Dorsey and Partners?</span></div>

    <p class="abs body-copy" style="left:32px;top:473px;width:330px">Dorsey and Partners puts patient care at the center of all we do. Whether you're dealing with a knee injury or chest congestion, Dorsey and Partners uses cutting edge cloud-based image storage to transfer images and return a final report to you within 24 hours.&nbsp; You can be confident that our radiologists will deliver consistent, accurate, and timely reports that will have a meaningful impact in your care plan and treatment decisions.</p>

    <div class="abs contact" style="left:32px;top:628px">
      <p>To hear more about our outpatient<br>services or free in office set up, please contact</p>
      <div class="contact-line">
        <svg class="icon" viewBox="0 0 14 14" aria-hidden="true"><circle cx="7" cy="7" r="6.2" fill="none" stroke="#fff" stroke-width="1.2"/><circle cx="7" cy="5.2" r="1.9" fill="#fff"/><path d="M3.8,11 C4.2,8.4 9.8,8.4 10.2,11 Z" fill="#fff"/></svg>
        <span>Dr. Elena Marsh</span>
        <svg class="icon" viewBox="0 0 14 14" aria-hidden="true"><circle cx="7" cy="7" r="6.2" fill="none" stroke="#fff" stroke-width="1.2"/><path d="M4.6,3.8 L5.9,3.6 L6.5,5.4 L5.7,6.1 C6.1,7 6.9,7.9 7.9,8.3 L8.6,7.5 L10.3,8.1 L10.2,9.4 C8.9,10.4 4,8.2 4.6,3.8 Z" fill="#fff"/></svg>
        <span>555-014-2297</span>
      </div>
    </div>
  </section>

  <!-- BACK -->
  <section class="page page--back">
    <svg class="abs" style="left:0;top:0;width:541px;height:120px" viewBox="0 0 541 120" aria-hidden="true"><polygon points="214,0 541,0 541,95 330,72" fill="var(--brand-red)"/></svg>

    <svg class="abs section-tab" style="left:0;top:32px;width:260px;height:36px" viewBox="0 0 260 36" preserveAspectRatio="none" aria-hidden="true"><polygon points="0,0 260,0 232,36 0,36" fill="var(--tab-dark)"/></svg>
    <div class="abs section-tab" style="left:0;top:32px;width:260px;height:36px"><span>Our Outpatient Services</span></div>

    <p class="abs body-copy body-copy--small" style="left:32px;top:74px;width:240px">We identified a need in our communities to provide a better product for our physicians when choosing office based imaging. In 2015 we began working with Verity Cloud to provide image interpretation while utilizing state of the art medical data and image management.&nbsp; As a physician owned practice, we pride ourselves on providing high quality and accurate reports with rapid results (a final report within 24 hours). We offer a 24 hour direct phone line for referring physicians to speak with one of our radiologists should a problem arise after hours.</p>

    <svg class="abs" style="left:270px;top:40px;width:271px;height:240px" viewBox="0 0 271 240" aria-hidden="true">
      <circle cx="188" cy="126" r="108" fill="#e2e2e3"/>
      <circle cx="188" cy="126" r="102" fill="#fff"/>
      <circle cx="76" cy="66" r="62" fill="#e2e2e3"/>
      <circle cx="76" cy="66" r="57" fill="#fff"/>
    </svg>
    <div class="abs" role="img" aria-label="Chest radiograph" style="left:362px;top:70px;width:192px;height:192px;border-radius:50%;background:radial-gradient(circle at 45% 50%, #3a3a3a 0%, #8a8a8a 45%, #d9d9d9 80%, #f4f4f4 100%)"></div>
    <div class="abs" role="img" aria-label="Hand radiograph" style="left:294px;top:58px;width:104px;height:104px;border-radius:50%;background:radial-gradient(circle at 50% 45%, #e6e6e6 0%, #8d8d8d 35%, #2c2c2c 75%, #1a1a1a 100%)"></div>

    <div class="photo photo--family" role="img" aria-label="Smiling family of four posing together outdoors"></div>
    <div class="abs headline-box"></div>
    <p class="abs headline">We look forward to being a complete solution for all of your imaging needs.</p>

    <svg class="abs section-tab" style="left:0;top:421px;width:144px;height:34px" viewBox="0 0 144 34" preserveAspectRatio="none" aria-hidden="true"><polygon points="0,0 144,0 118,34 0,34" fill="var(--tab-dark)"/></svg>
    <div class="abs section-tab" style="left:0;top:421px;width:144px;height:34px"><span>Our Staff</span></div>

    <svg class="abs footer-wave" viewBox="0 0 541 120" preserveAspectRatio="none" aria-hidden="true"><path d="M0,78 C80,116 160,100 230,52 C320,12 440,2 541,0 L541,120 L0,120 Z" fill="var(--brand-red)"/></svg>

    <p class="abs body-copy body-copy--small" style="left:32px;top:462px;width:228px">The radiologists and staff of Dorsey and Partners are committed to serving as partners in exceptional patient care. Dorsey and Partners is comprised of some of the most talented radiologists in the Metro Lakeshore Area, with sub-specialty expertise in advanced musculoskeletal radiology, chest radiology, sports injury, ultrasound, obstetric ultrasound and much more. Our radiologists have trained at some of the most respected medical facilities in the country and understand the importance of continuing education, innovation and staying engaged in our evolving field.</p>
    <p class="abs body-copy body-copy--small" style="left:282px;top:462px;width:228px">With our dedication to quality patient care, the doctors and staff of Dorsey and Partners go above and beyond to assure your office needs are met. We will work with you through image interpretation, imaging follow-up, and are committed to your confidence in our process. Our goal is to help you integrate our services to create a superior diagnostic and treatment process that works for you and your practice.</p>

    <div class="abs contact contact--right" style="right:31px;top:630px">
      <p>To hear more about our outpatient<br>services or free in office set up, please contact</p>
      <div class="contact-line">
        <svg class="icon" viewBox="0 0 14 14" aria-hidden="true"><circle cx="7" cy="7" r="6.2" fill="none" stroke="#fff" stroke-width="1.2"/><circle cx="7" cy="5.2" r="1.9" fill="#fff"/><path d="M3.8,11 C4.2,8.4 9.8,8.4 10.2,11 Z" fill="#fff"/></svg>
        <span>Dr. Elena Marsh</span>
        <svg class="icon" viewBox="0 0 14 14" aria-hidden="true"><circle cx="7" cy="7" r="6.2" fill="none" stroke="#fff" stroke-width="1.2"/><path d="M4.6,3.8 L5.9,3.6 L6.5,5.4 L5.7,6.1 C6.1,7 6.9,7.9 7.9,8.3 L8.6,7.5 L10.3,8.1 L10.2,9.4 C8.9,10.4 4,8.2 4.6,3.8 Z" fill="#fff"/></svg>
        <span>555-014-2297</span>
      </div>
    </div>
  </section>

</main>
</body>
</html>
```